Letterhead, envelope & business card design

We would like to refresh the look and feel of our business cards & letterheads.

Our company specialises in premium property.

We are looking for a unique minimalist design for our letterhead & business cards that project this.

I can send over examples of our current design to draw from, although Im looking for some one with creativity, yet focussed on a clean modern, minimalist design.
Updates

I have just uploaded our current letterhead.

We have just removed the 'swoosh' grey symbol, but would still like to keep some part of grey in the design if possible.

thanks in advance.

Just uploaded my details for business card.

Can we see examples with the light grey used as the secondary color?

thanks in advance.

Target Market(s)

We are a premium real estate agency & we want that message to be carried through our business cards & stationery.

Industry/Entity Type

Business

```html
<!DOCTYPE html>
<html lang="en">
<head>
<meta charset="utf-8">
<title>Hartwell Estate Agents – Business Card</title>
<link href="https://fonts.googleapis.com/css2?family=Arimo:wght@400&display=swap" rel="stylesheet">
<style>
  :root {
    --page-bg: #f3f3f3;
    --card-bg: #ffffff;
    --band-light: #2a8db4;
    --band-mid: #1d7a9f;
    --band-dark: #134f69;
    --wordmark: #1d3f55;
    --text-grey: #8c8c8c;
    --rule-grey: #a5a5a5;
    --on-band: #ffffff;
  }
  * { margin: 0; padding: 0; box-sizing: border-box; }
  html, body {
    width: 1200px;
    height: 681px;
    overflow: hidden;
    background: var(--page-bg);
    font-family: "Arimo", Arial, sans-serif;
  }
  .card {
    position: absolute;
    left: 344px;
    width: 511px;
    height: 297px;
    background: var(--card-bg);
    box-shadow: 0 2px 8px rgba(0, 0, 0, 0.18);
  }
  .card--back { top: 14px; }
  .card--front { top: 368px; }

  .brand-band {
    position: absolute;
    background: linear-gradient(100deg, var(--band-mid) 0%, var(--band-light) 38%, var(--band-mid) 62%, var(--band-dark) 100%);
  }
  .card--back .brand-band { left: 0; top: 119px; width: 100%; height: 60px; }
  .card--front .brand-band { left: 0; top: 118px; width: 238px; height: 59px; }

  .contact-block {
    position: absolute;
    left: 25px;
    padding-left: 13px;
    border-left: 1px solid var(--rule-grey);
    color: var(--text-grey);
    font-size: 13.5px;
    line-height: 17px;
  }
  .contact-block--sales { top: 8px; }
  .contact-block--leasing { top: 184px; }
  .contact-block .dept { text-transform: uppercase; }
  .contact-block .email { font-size: 9.5px; line-height: 16px; }

  .wordmark {
    position: absolute;
    font-family: "Arimo", Arial, sans-serif;
    font-weight: 400;
    letter-spacing: 1px;
    text-transform: uppercase;
  }
  .card--back .wordmark {
    right: 48px;
    top: 131px;
    font-size: 34px;
    line-height: 36px;
    color: var(--on-band);
  }
  .card--front .wordmark {
    left: 266px;
    top: 118px;
    font-size: 38px;
    line-height: 40px;
    color: var(--wordmark);
  }
  .web-address {
    position: absolute;
    left: 284px;
    top: 160px;
    font-size: 12.5px;
    color: var(--text-grey);
  }
</style>
</head>
<body>
  <section class="card card--back">
    <div class="contact-block contact-block--sales">
      <p class="dept">Sales</p>
      <p>52 Harbour Rd</p>
      <p>Lindale NSW 2290</p>
      <p>T. 02 5550 1188</p>
      <p>F. 02 5550 1187</p>
      <p class="email">management@hartwellestates.com.au</p>
    </div>
    <div class="brand-band"></div>
    <p class="wordmark">Hartwell</p>
    <div class="contact-block contact-block--leasing">
      <p class="dept">Property Management</p>
      <p>52 Harbour Rd</p>
      <p>Lindale NSW 2290</p>
      <p>T. 02 5550 1102</p>
      <p>F. 02 5550 1187</p>
      <p class="email">leasing@hartwellestates.com.au</p>
    </div>
  </section>

  <section class="card card--front">
    <div class="brand-band"></div>
    <p class="wordmark">Hartwell</p>
    <p class="web-address">www.hartwellestates.com.au</p>
  </section>
</body>
</html>
```